lab equipment website

We need a fresh new look for a company website called quorvin. We will be using the current logo and brand colors on their current website quorvin.com. They want to keep their text and on-page SEO, but would like to reformat it to look more modern and fresh. They want to have everything be high performance with a great user experience. Their main call to action is for people to fill in a contact form so they can call them. There is some information that is purposely above the fold on the instrument pages. I will need the home page, about page and a leasing page.

```html
<!DOCTYPE html>
<html lang="en">
<head>
<meta charset="utf-8">
<title>quorvin – Lab Equipment Support & Leasing</title>
<link href="https://fonts.googleapis.com/css2?family=Montserrat:wght@500;600;700&family=Open+Sans:wght@400;600;700&display=swap" rel="stylesheet">
<style>
:root{
  --teal:#1cb5a3;
  --teal-dark:#0f7a70;
  --teal-deep:#0b4f52;
  --ink:#222a30;
  --body:#5d666c;
  --line:#e1e6e8;
  --skill-bg:#e4eff3;
  --footer:#2e3439;
  --white:#ffffff;
}
*{box-sizing:border-box;margin:0;padding:0}
html,body{width:1200px;height:4749px;overflow:hidden}
body{font-family:"Open Sans",Arial,sans-serif;color:var(--body);background:var(--white);position:relative}
h1,h2,h3,.nav,.btn,.brand{font-family:"Montserrat",Arial,sans-serif}
.abs{position:absolute}
.section{position:absolute;left:0;width:1200px}
.btn{position:absolute;display:flex;align-items:center;justify-content:center;background:var(--teal);color:var(--white);font-weight:700;font-size:17px;letter-spacing:.5px;text-transform:uppercase;width:200px;height:50px}
.btn.center{left:500px}
.btn.hex{clip-path:polygon(8% 0,92% 0,100% 50%,92% 100%,8% 100%,0 50%)}

/* header */
.site-header{top:0;height:127px;background:var(--white)}
.brand{position:absolute;left:78px;top:42px;display:flex;align-items:center;gap:10px;font-size:34px;font-weight:700;color:var(--ink)}
.brand .mark{width:26px;height:26px;background:var(--teal);border-radius:50%}
.topbar{position:absolute;right:70px;top:10px;display:flex;gap:24px;font-size:14px;color:var(--ink)}
.topbar span::before{content:"";display:inline-block;width:10px;height:10px;border-radius:50%;background:var(--teal);margin-right:8px}
.nav{position:absolute;left:430px;top:70px;display:flex;gap:34px;font-size:15px;font-weight:600;color:var(--ink)}
.nav .active{color:var(--teal)}
.search{position:absolute;left:860px;top:58px;width:262px;height:40px;border:1px solid var(--line);border-radius:20px;padding-left:18px;font-size:14px;line-height:38px;color:#9aa3a8}
.search i{position:absolute;right:4px;top:4px;width:30px;height:30px;border-radius:50%;background:var(--teal)}

/* hero */
.hero{top:127px;height:560px}
.hero .bg{position:absolute;inset:0;background:linear-gradient(120deg,#0b5658 0%,#127b74 45%,#1aa293 100%)}
.hero h1{position:absolute;top:145px;width:100%;text-align:center;color:var(--white);font-size:46px;line-height:54px;font-weight:700}
.hero p{position:absolute;top:270px;left:250px;width:700px;text-align:center;color:#dff3f0;font-size:16px;line-height:26px}
.hero .btn{top:340px}

/* features */
.features{top:600px;height:280px}
.feature{position:absolute;width:200px;text-align:center}
.feature svg{display:block;margin:0 auto}
.feature p{margin-top:20px;font-size:15px;line-height:26px;color:var(--ink)}
.divider{position:absolute;left:76px;top:900px;width:1048px;height:1px;background:var(--line)}

/* trusted */
.trusted{top:918px;height:475px}
.trusted h2{position:absolute;left:76px;top:40px;width:600px;font-size:36px;line-height:48px;color:var(--ink);font-weight:700}
.trusted p{position:absolute;left:76px;top:205px;width:580px;font-size:15px;line-height:27px}
.trusted .btn{left:76px;top:365px}
.trusted .visual{position:absolute;left:700px;top:20px;width:400px;height:440px;background:radial-gradient(circle,#e9f7f5 0%,#b8e6df 60%,#6ccabd 100%);clip-path:polygon(25% 0,75% 0,100% 50%,75% 100%,25% 100%,0 50%)}

/* needs */
.needs{top:1393px;height:747px;background:linear-gradient(180deg,#0d5d5e 0%,#12817a 55%,#1aa395 100%);color:var(--white)}
.needs h2{position:absolute;top:62px;width:100%;text-align:center;font-size:36px;line-height:46px;font-weight:700}
.needs .intro{position:absolute;top:170px;left:250px;width:700px;text-align:center;font-size:15px;line-height:25px;color:#d9f1ee}
.needs .photo{position:absolute;left:0;top:300px;width:520px;height:447px;background:linear-gradient(150deg,#e8eef2 0%,#bcd1da 60%,#7fa9b9 100%)}
.needs ul{position:absolute;left:540px;top:283px;width:580px;list-style:none;font-size:14px;line-height:20px;color:#e7f6f4}
.needs li{position:relative;padding-left:32px;margin-bottom:20px}
.needs li::before{content:"";position:absolute;left:0;top:1px;width:18px;height:18px;border-radius:50%;background:var(--teal)}
.needs li::after{content:"";position:absolute;left:5px;top:5px;width:7px;height:4px;border-left:2px solid #fff;border-bottom:2px solid #fff;transform:rotate(-45deg)}
.needs .closing{position:absolute;left:540px;top:590px;width:580px;font-size:14px;line-height:24px;color:#e7f6f4}

/* skills */
.skills{top:2140px;height:377px;background:var(--skill-bg)}
.skills h2{position:absolute;top:62px;width:100%;text-align:center;font-size:36px;color:var(--ink);font-weight:700}
.skill{position:absolute;top:148px;width:200px;text-align:center}
.skill svg{display:block;margin:0 auto}
.skill .val{position:absolute;top:46px;width:100%;font-family:"Montserrat",Arial,sans-serif;font-weight:700;font-size:26px;color:var(--ink)}
.skill h3{margin-top:22px;font-size:15px;font-weight:700;color:var(--ink)}

/* leasing */
.leasing{top:2517px;height:760px}
.leasing h2{position:absolute;top:72px;width:100%;text-align:center;font-size:38px;color:var(--ink);font-weight:700}
.leasing .products{position:absolute;left:180px;top:170px;width:850px;height:250px;background:linear-gradient(90deg,#d7dde1 0%,#f1f3f5 50%,#cfd6db 100%)}
.leasing p{position:absolute;left:215px;top:465px;width:770px;text-align:center;font-size:15px;line-height:28px}
.leasing .btn{top:653px}

/* testimonial */
.testimonial{top:3277px;height:364px;background:linear-gradient(120deg,#0c5559 0%,#13847b 55%,#1aa495 100%);color:var(--white)}
.testimonial h2{position:absolute;top:50px;width:100%;text-align:center;font-size:38px;font-weight:700}
.testimonial .avatar{position:absolute;left:195px;top:165px;width:92px;height:92px;border-radius:50%;background:#cfe3e1;border:3px solid rgba(255,255,255,.6)}
.testimonial blockquote{position:absolute;left:325px;top:152px;width:690px;font-size:15px;line-height:27px;color:#e4f5f3}
.testimonial .author{position:absolute;left:905px;top:282px;font-family:"Montserrat",Arial,sans-serif;font-weight:700;font-size:16px}
.testimonial .author::before{content:"";position:absolute;left:-52px;top:10px;width:38px;height:2px;background:#fff}
.testimonial .role{position:absolute;left:905px;top:306px;font-size:13px;color:#d9f1ee}
.arrow{position:absolute;top:165px}

/* contact */
.contact{top:3641px;height:734px}
.contact h2{position:absolute;top:150px;width:100%;text-align:center;font-size:40px;color:var(--ink);font-weight:700}
.contact .lead{position:absolute;top:218px;left:330px;width:540px;text-align:center;font-size:15px;line-height:25px}
.field{position:absolute;left:320px;width:560px;height:44px;border:1px solid var(--line);padding-left:16px;font-size:13px;line-height:42px;color:#8b949a;background:var(--white)}
.field.select::after{content:"";position:absolute;right:18px;top:16px;width:7px;height:7px;border-right:2px solid #8b949a;border-bottom:2px solid #8b949a;transform:rotate(45deg)}
.field.message{height:100px}
.contact .btn{top:622px;width:160px;left:520px}

/* footer */
.site-footer{top:4375px;height:311px;background:var(--footer);color:#c4cbcf}
.site-footer .brand{left:110px;top:54px;color:var(--white)}
.social{position:absolute;left:110px;top:150px;display:flex;gap:10px}
.social span{width:38px;height:38px;border-radius:50%;background:var(--teal)}
.fcol{position:absolute;top:48px;font-size:14px;line-height:26px}
.fcol h3{font-size:16px;font-weight:700;color:var(--white);margin-bottom:12px;letter-spacing:.5px}
.fcol li{list-style:none;position:relative;padding-left:16px}
.fcol li::before{content:"";position:absolute;left:0;top:11px;width:5px;height:5px;border-radius:50%;background:var(--teal)}
.newsletter{position:absolute;left:875px;top:188px;width:248px;height:44px;background:var(--white);padding-left:14px;font-size:13px;line-height:44px;color:#8b949a}
.site-footer .btn{left:875px;top:248px;width:180px;height:44px;font-size:16px}
.copy{position:absolute;left:0;top:4686px;width:1200px;height:63px;background:var(--teal);color:var(--white);text-align:center;font-size:13px;line-height:63px}
</style>
</head>
<body>

<header class="section site-header">
  <div class="brand"><span class="mark"></span>quorvin</div>
  <div class="topbar"><span>(415) 555-0142</span><span>info@quorvin.com</span></div>
  <nav class="nav"><span class="active">HOME</span><span>ABOUT</span><span>LEASING</span><span>FAQ</span><span>CONTACT</span></nav>
  <div class="search">Search...<i></i></div>
</header>

<section class="section hero">
  <div class="bg" role="img" aria-label="Laboratory glassware and equipment photo with a teal overlay"></div>
  <svg class="abs" style="left:0;bottom:0" width="1200" height="160" viewBox="0 0 1200 160"><polygon points="0,40 600,160 1200,40 1200,160 0,160" fill="#ffffff"/></svg>
  <h1>Our Goal is Simple Save Labs<br>Time And Money</h1>
  <p>quorvin is a lab support program that provides scientists with comprehensive maintenance/repair coverage and operating lease solutions at an affordable price.</p>
  <a class="btn center hex">Learn More</a>
</section>

<section class="section features">
  <div class="feature" style="left:258px">
    <svg width="120" height="130" viewBox="0 0 120 130"><polygon points="60,4 114,34 114,96 60,126 6,96 6,34" fill="#fff" stroke="#1cb5a3" stroke-width="4"/><rect x="36" y="48" width="48" height="36" rx="4" fill="none" stroke="#222a30" stroke-width="3"/><path d="M50 48v-6h20v6M60 58v16M52 66h16" stroke="#222a30" stroke-width="3" fill="none"/></svg>
    <p>Worry-Free lab<br>Equipment PM/repair<br>Coverage.</p>
  </div>
  <div class="feature" style="left:495px">
    <svg width="120" height="130" viewBox="0 0 120 130"><polygon points="60,4 114,34 114,96 60,126 6,96 6,34" fill="#fff" stroke="#1cb5a3" stroke-width="4"/><path d="M52 40l14 0M58 40l-8 30M44 88h36M60 88c12 0 18-10 14-22" stroke="#222a30" stroke-width="3" fill="none"/><circle cx="50" cy="74" r="5" fill="none" stroke="#222a30" stroke-width="3"/></svg>
    <p>Cost-effective lease<br>structures and payment<br>plans.</p>
  </div>
  <div class="feature" style="left:733px">
    <svg width="120" height="130" viewBox="0 0 120 130"><polygon points="60,4 114,34 114,96 60,126 6,96 6,34" fill="#fff" stroke="#1cb5a3" stroke-width="4"/><path d="M52 40h16M55 40v18l-14 28h38l-14-28V40" stroke="#222a30" stroke-width="3" fill="none"/><path d="M46 76h28" stroke="#1cb5a3" stroke-width="3"/></svg>
    <p>Knowledge of the<br>laboratory.</p>
  </div>
</section>
<div class="divider"></div>

<section class="section trusted">
  <h2>Trusted Company Offering Scientific Equipment Service Plans and Flexible Leases</h2>
  <p>At quorvin, our goal is to ensure the success of your business. Whether you are running a laboratory or other scientific facilities, we want to keep you provided with the best in cutting-edge equipment. That's why we offer flexible scientific equipment leasing options with worry-free service plans to provide your business with the tools needed to perform at its peak.</p>
  <a class="btn hex">Learn More</a>
  <div class="visual" role="img" aria-label="Laboratory microscope inside layered teal hexagons"></div>
</section>

<section class="section needs">
  <h2>We Understand Your Needs Because<br>We Are Scientists First</h2>
  <p class="intro">When it comes to creating innovative solutions that cater to your lab, quorvin's dedicated team of problem-solvers has got you covered. Here's how we save you time and money:</p>
  <div class="photo" role="img" aria-label="Photo of two scientists working with a microscope and samples"></div>
  <ul>
    <li>We collaborate with you directly—no middlemen!</li>
    <li>We handle scientific equipment service, repairs, and maintenance</li>
    <li>We consolidate and streamline the ancillary work associated with lab equipment procurement and service</li>
    <li>We utilize our networks to bring you the most cost-savings possible</li>
    <li>We improve cash flow by removing the upfront cost of purchasing, freeing up capital in your everyday budget</li>
    <li>We may provide tax advantages with our lease structures</li>
  </ul>
  <p class="closing">We regularly provide businesses with what they need to improve their budget and efficiency. We offer laboratory equipment leasing for a wide range of needs. If you want to discuss your needs more in-depth, don't hesitate to call us at (415) 555-0142 or fill out our contact form.</p>
</section>

<section class="section skills">
  <h2>Our Skill</h2>
  <div class="skill" style="left:65px"><svg width="130" height="130" viewBox="0 0 130 130"><circle cx="65" cy="65" r="56" fill="none" stroke="#ffffff" stroke-width="8"/><circle cx="65" cy="65" r="56" fill="none" stroke="#0f7a70" stroke-width="8" stroke-dasharray="281.5 351.9" transform="rotate(-90 65 65)"/></svg><div class="val">80%</div><h3>Cost Saving</h3></div>
  <div class="skill" style="left:267px"><svg width="130" height="130" viewBox="0 0 130 130"><circle cx="65" cy="65" r="56" fill="none" stroke="#ffffff" stroke-width="8"/><circle cx="65" cy="65" r="56" fill="none" stroke="#0f7a70" stroke-width="8" stroke-dasharray="316.7 351.9" transform="rotate(-90 65 65)"/></svg><div class="val">90%</div><h3>Lease Plan Flexibility</h3></div>
  <div class="skill" style="left:492px"><svg width="130" height="130" viewBox="0 0 130 130"><circle cx="65" cy="65" r="56" fill="none" stroke="#0f7a70" stroke-width="8"/></svg><div class="val">100%</div><h3>Customer Service</h3></div>
  <div class="skill" style="left:720px"><svg width="130" height="130" viewBox="0 0 130 130"><circle cx="65" cy="65" r="56" fill="none" stroke="#ffffff" stroke-width="8"/><circle cx="65" cy="65" r="56" fill="none" stroke="#0f7a70" stroke-width="8" stroke-dasharray="158.4 351.9" transform="rotate(-90 65 65)"/></svg><div class="val">45%</div><h3>Reliability</h3></div>
  <div class="skill" style="left:932px"><svg width="130" height="130" viewBox="0 0 130 130"><circle cx="65" cy="65" r="56" fill="none" stroke="#ffffff" stroke-width="8"/><circle cx="65" cy="65" r="56" fill="none" stroke="#0f7a70" stroke-width="8" stroke-dasharray="52.8 351.9" transform="rotate(-90 65 65)"/></svg><div class="val">15%</div><h3>Continued Support</h3></div>
</section>

<section class="section leasing">
  <h2>Leasing</h2>
  <div class="products" role="img" aria-label="Row of lab instruments: centrifuge, incubator, autoclave, microscope and analytical balance"></div>
  <p>So why our laboratory equipment leasing program? Because when capital is limited, purchasing equipment poses a serious burden. Fortunately there is a solution: quorvin. Our laboratory support services allow you to use equipment for a fraction of the price as well as the freedom to utilize different machines for various lengths of time, instead of being tied down to a single machine. Plus, when you collaborate with quorvin and anything goes wrong with our machine, we've got your back with our stress-free repair coverage. With quorvin's all-inclusive equipment packages, there is an affordable solution to an expensive problem.</p>
  <a class="btn center hex">Learn More</a>
</section>

<section class="section testimonial">
  <h2>What Our Clent Say</h2>
  <svg class="arrow" style="left:80px" width="20" height="36" viewBox="0 0 20 36"><path d="M17 2L3 18l14 16" stroke="#ffffff" stroke-opacity=".6" stroke-width="3" fill="none"/></svg>
  <svg class="arrow" style="left:1100px" width="20" height="36" viewBox="0 0 20 36"><path d="M3 2l14 16L3 34" stroke="#ffffff" stroke-opacity=".6" stroke-width="3" fill="none"/></svg>
  <div class="avatar" role="img" aria-label="Client portrait"></div>
  <blockquote>My time spent in the lab opened my eyes to the passion and dedication that drives scientists, as well as the frustration of a tight budget and equipment upkeep. quorvin was created in order to help overcome these obstacles and enable scientists to focus on what they're truly passionate about: research.</blockquote>
  <div class="author">DANA PRICE</div>
  <div class="role">Lab Relations</div>
</section>

<section class="section contact">
  <h2>Further questions?</h2>
  <p class="lead">Feel free to contact us if you have any questions or comments. We promise to get back to you within 24 hours.</p>
  <div class="field" style="top:294px">Name *</div>
  <div class="field" style="top:349px">Phone *</div>
  <div class="field" style="top:404px">Email *</div>
  <div class="field select" style="top:459px">Leasing *</div>
  <div class="field message" style="top:514px">Message *</div>
  <a class="btn hex">Submit</a>
</section>

<footer class="section site-footer">
  <div class="brand"><span class="mark"></span>quorvin</div>
  <div class="social"><span></span><span></span><span></span><span></span></div>
  <div class="fcol" style="left:345px"><h3>SITEMAP</h3><ul><li>Home</li><li>About</li><li>Leasing</li><li>Faq</li><li>Contact</li></ul></div>
  <div class="fcol" style="left:608px"><h3>CONTACT US</h3><ul><li>quorvin Inc.<br>220 Harbor Lane Suite 410<br>Oakland, CA 94607</li><li>(415) 555-0142</li><li>info@quorvin.com</li><li>https://quorvin.com</li></ul></div>
  <div class="fcol" style="left:875px;width:250px;line-height:22px"><h3>CONTACT US</h3><p>Would you like to receive our exclusive news and update for signup our newsletter !</p></div>
  <div class="newsletter">Enter Email *</div>
  <a class="btn hex">Subscribe</a>
</footer>
<div class="copy">©quorvin - 2018 All Right Reserved</div>

</body>
</html>
```